Dorm Treasury Wordpress Website (re)design

we are a student run financial literacy website and are desperately trying to get college students to pay attention to the finances to create solid financial skills for life. This age group LOVES instagram so instead of sharing a lot of text we want to tease through graphics/infographics topics that are relevant to them based on what their peers are discussing and then push them to our resources to learn more. ultimately we will also recommend products to them that are carefully selected by us. these will range from a book on paying back their student loan to a place to store their dorm stuff when they go home for summer break to a credit card we determine is best for them. So yes, commerce is imp but SEO to attract students comes first which we will do through survey monkey and cash prizes. we need to capture email address. we also have a "checklist" (attached and needs rebranding) of the basic and most imp money matters for them. Each item will hyperlink to our parnter, Tallyvane, and need to do so seamlessly and push them back to us.

college students and young adults

• simple, clean and graphic with an integration of survey monkey, an amazon store and a capture of emails through mailchimp or other similar. Ability to edit after ourselves on wordpress

```html
<!DOCTYPE html>
<html lang="en">
<head>
<meta charset="utf-8">
<title>Dorm Treasury — Take charge of your change</title>
<link rel="stylesheet" href="https://fonts.googleapis.com/css2?family=Lato:wght@400;700&family=Prata&display=swap">
<style>
:root{
  --blue:#16649f;
  --green:#5db438;
  --green-soft:#7cbf5c;
  --ink:#333;
  --ink-soft:#555;
  --grey-bg:#f4f4f4;
  --white:#fff;
  --serif:'Prata',Georgia,serif;
  --sans:'Lato',Arial,sans-serif;
}
*{box-sizing:border-box;margin:0;padding:0}
html,body{width:1200px;height:3632px;overflow:hidden}
body{position:relative;background:var(--white);font-family:var(--sans);color:var(--ink)}
h1,h2,h3{font-weight:400}

/* header */
.site-header{position:absolute;left:0;top:0;width:1200px;height:131px;border-top:3px solid var(--green);background:var(--white)}
.brand{position:absolute;left:113px;top:52px;display:flex;align-items:center;gap:10px}
.brand-name{font-family:var(--sans);font-weight:700;font-size:30px;color:var(--blue);letter-spacing:-.5px}
.brand-dot{width:22px;height:22px;border-radius:50%;background:var(--green)}
.login{position:absolute;left:987px;top:19px;width:100px;height:42px;border-radius:21px;background:var(--green);color:var(--white);font-weight:700;font-size:15px;display:flex;align-items:center;justify-content:center}
.main-nav{position:absolute;top:89px;left:0;font-size:12px;font-weight:700;letter-spacing:.3px;color:#222}
.main-nav span{position:absolute;white-space:nowrap}
.main-nav .current{color:var(--green)}

/* hero */
.hero{position:absolute;left:0;top:131px;width:1200px;height:708px;overflow:hidden}
.hero-photo{position:absolute;inset:0;background:linear-gradient(100deg,#5f7f4e 0%,#7d9a69 35%,#a7b497 55%,#6d8fb0 75%,#4d6f93 100%)}
.hero-title{position:absolute;left:111px;top:232px;font-family:var(--serif);font-size:50px;color:var(--white);letter-spacing:1px;white-space:nowrap}
.hero-text{position:absolute;left:112px;top:310px;width:370px;font-size:14.5px;line-height:30px;color:var(--white)}
.btn-gradient{position:absolute;left:113px;top:451px;width:144px;height:52px;border-radius:26px;background:linear-gradient(90deg,#5db438,#1e7da3);color:var(--white);font-size:16px;display:flex;align-items:center;justify-content:center}
.hero-curve{position:absolute;left:0;bottom:0;width:1200px;height:170px}

/* welcome */
.eyebrow{position:absolute;left:0;width:1200px;text-align:center;font-family:var(--serif);font-size:16px;color:#222}
.section-title{position:absolute;left:0;width:1200px;text-align:center;font-family:var(--serif);color:var(--green)}
.welcome-text{position:absolute;left:262px;top:994px;width:676px;text-align:center;font-size:13px;line-height:30px;color:var(--ink)}

/* feature cards */
.card{position:absolute;top:1206px;width:298px;height:389px;border-radius:6px;color:var(--white);text-align:center}
.card.blue{background:var(--blue)}
.card.green{background:var(--green)}
.card svg{position:absolute;left:50%;top:28px;transform:translateX(-50%)}
.card-title{position:absolute;left:20px;right:20px;top:144px;font-family:var(--serif);font-size:16px;line-height:26px;letter-spacing:.3px}
.card-rule{position:absolute;left:50%;width:28px;margin-left:-14px;height:2px;background:var(--white)}
.card-text{position:absolute;left:24px;right:24px;font-size:13px;line-height:27px}
.btn-outline{position:absolute;left:50%;top:318px;width:134px;height:47px;margin-left:-67px;border:1.5px solid var(--white);border-radius:24px;font-size:15px;display:flex;align-items:center;justify-content:center}

/* course band */
.course-band{position:absolute;left:0;top:1734px;width:1200px;height:418px;background:var(--green)}
.checklist{position:absolute;left:121px;top:1693px;width:392px;height:501px;background:var(--white);border:1px solid #bbb;padding:6px;box-shadow:0 2px 6px rgba(0,0,0,.15)}
.checklist-art{width:100%;height:100%;border:2px solid #444;background:linear-gradient(180deg,#fff 0%,#fff 8%,#b8e0f5 8%,#a9d8f2 92%,#fff 92%)}
.course-title{position:absolute;left:556px;top:1803px;font-family:var(--serif);font-size:27px;line-height:44px;color:var(--white);letter-spacing:.5px}
.course-text{position:absolute;left:557px;top:1915px;width:520px;font-size:13px;line-height:27px;color:var(--white)}
.course-cta{position:absolute;left:557px;top:2021px;width:530px;font-size:16px;line-height:27px;color:var(--white)}

/* testimonials */
.quote-card{position:absolute;top:2363px;width:311px;height:228px;border:1px solid var(--green-soft);background:var(--white)}
.quote-badge{position:absolute;left:22px;top:-28px;width:60px;height:60px;border-radius:50%;background:var(--green);display:flex;align-items:center;justify-content:center}
.quote-body{position:absolute;left:30px;right:22px;top:62px}
.quote-text{font-size:13px;line-height:26px;color:var(--ink-soft)}
.quote-author{margin-top:16px;font-size:12px;color:var(--ink)}
.quote-author b{font-weight:400;color:var(--green);font-size:14px}

/* blog */
.blog-section{position:absolute;left:0;top:2662px;width:1200px;height:683px;background:var(--grey-bg)}
.title-rule{position:absolute;left:570px;top:2743px;width:60px;height:3px;background:var(--blue)}
.post-feature{position:absolute;left:113px;top:2795px;width:474px;height:488px;background:var(--white);box-shadow:0 1px 4px rgba(0,0,0,.08)}
.post-feature .thumb{height:279px;background:linear-gradient(180deg,#3f79b8 0%,#6fa0d0 60%,#2c3440 85%,#1e232b 100%)}
.post-title{font-family:var(--serif);font-size:16px;color:#222}
.post-meta{font-family:var(--serif);font-style:italic;font-size:11px;color:var(--green)}
.post-excerpt{font-size:12px;line-height:25px;color:var(--ink-soft)}
.post-small{position:absolute;left:612px;width:475px;height:152px;background:var(--white);box-shadow:0 1px 4px rgba(0,0,0,.08)}
.post-small .thumb{position:absolute;left:8px;top:6px;width:143px;height:140px}
.post-small .body{position:absolute;left:169px;top:22px;right:12px}

/* footer */
.site-footer{position:absolute;left:0;top:3345px;width:1200px;height:287px;background:var(--blue);color:var(--white);text-align:center}
.footer-brand{position:absolute;left:0;width:1200px;top:68px;display:flex;justify-content:center;align-items:center;gap:12px}
.footer-brand .brand-name{color:var(--white);font-size:40px}
.footer-brand .brand-dot{width:28px;height:28px;background:var(--white)}
.footer-nav{position:absolute;left:0;width:1200px;top:154px;font-family:var(--serif);font-size:14px}
.footer-nav span{margin:0 14px}
.copyright{position:absolute;left:0;width:1200px;top:209px;font-family:var(--serif);font-size:14px}
</style>
</head>
<body>

<header class="site-header">
  <div class="brand"><span class="brand-name">Dorm Treasury</span><span class="brand-dot"></span></div>
  <div class="login">LOGIN</div>
  <nav class="main-nav">
    <span class="current" style="left:442px">HOME</span>
    <span style="left:526px">TAKE THE PLEDGE</span>
    <span style="left:683px">BLOG</span>
    <span style="left:763px">ABOUT US</span>
    <span style="left:872px">TIPS &amp; TRICKS</span>
    <span style="left:985px">ABOUT TALLYVANE</span>
  </nav>
</header>

<section class="hero">
  <div class="hero-photo" role="img" aria-label="Photo of a smiling graduate in a cap holding a blue piggy bank against a soft green background"></div>
  <h1 class="hero-title">DORM TREASURY</h1>
  <p class="hero-text">Our mission is simple: To provide a comprehensive resource that enables college students and young adults to gain a better understanding of financial them succeed in their careers and in life.</p>
  <div class="btn-gradient">Read More</div>
  <svg class="hero-curve" viewBox="0 0 1200 170" preserveAspectRatio="none">
    <path d="M0 60 Q600 250 1200 40 L1200 170 L0 170 Z" fill="#fff"/>
    <path d="M140 98 Q600 258 1060 94" fill="none" stroke="#5db438" stroke-width="5"/>
  </svg>
</section>

<div class="eyebrow" style="top:890px">WELCOME</div>
<h2 class="section-title" style="top:920px;font-size:38px">DORM TREASURY</h2>
<p class="welcome-text">Welcome to your FREE resource that will help you achieve financial independence and knowledge.Using peer-peer tips, personal stories and Tallyvane, you can become a Dorm Treasury pro!Dorm Treasury’s roots go back to 2011 when Helen Carver, a CPA and Financial Planner, founded ‘DivaLedger’ with her daughter, Clara. DivaLedger financial literacy initiative that focused on educating women. It didn’t take long before DivaLedger’s college interns spoke up about the importance of having personal financial skills in their own lives</p>

<article class="card blue" style="left:113px">
  <svg width="100" height="96" viewBox="0 0 100 96" fill="none" stroke="#fff" stroke-width="3">
    <circle cx="30" cy="52" r="22"/><circle cx="62" cy="26" r="20"/><circle cx="66" cy="68" r="24" fill="#fff"/>
    <text x="30" y="61" font-family="Lato" font-size="26" font-weight="700" fill="#fff" stroke="none" text-anchor="middle">$</text>
    <text x="62" y="35" font-family="Lato" font-size="24" font-weight="700" fill="#fff" stroke="none" text-anchor="middle">$</text>
    <text x="66" y="78" font-family="Lato" font-size="28" font-weight="700" fill="#16649f" stroke="none" text-anchor="middle">$</text>
  </svg>
  <h3 class="card-title">HOW TO BUDGET</h3>
  <div class="card-rule" style="top:182px"></div>
  <p class="card-text" style="top:192px">Having a solid budget is a fundamental building block in becoming financially independent, here is a breakdown of the and stick to your own budget</p>
  <div class="btn-outline">Read More!</div>
</article>

<article class="card green" style="left:451px">
  <svg width="100" height="90" viewBox="0 0 100 90" fill="none" stroke="#fff" stroke-width="3">
    <rect x="4" y="32" width="92" height="50"/><rect x="12" y="40" width="76" height="34"/>
    <path d="M38 32 V20 a12 12 0 0 1 24 0 V32"/>
    <circle cx="50" cy="57" r="14"/>
    <text x="50" y="64" font-family="Lato" font-size="18" font-weight="700" fill="#fff" stroke="none" text-anchor="middle">$</text>
  </svg>
  <h3 class="card-title">MONEY SAVING HACKS<br>FOR MILLENNIALS</h3>
  <div class="card-rule" style="top:208px"></div>
  <p class="card-text" style="top:220px">The other generations love to pick on us, but the unemployment rate is the lowest it’s been in over 50 years</p>
  <div class="btn-outline">Read More!</div>
</article>

<article class="card blue" style="left:790px">
  <svg width="100" height="96" viewBox="0 0 100 96" fill="none" stroke="#fff" stroke-width="3">
    <circle cx="40" cy="42" r="28"/><path d="M40 24 V42 L54 50"/>
    <path d="M4 74 H34 M10 82 H40 M16 90 H46" stroke-linecap="round"/>
    <path d="M74 20 L92 20 M78 30 L96 30" stroke-linecap="round"/>
  </svg>
  <h3 class="card-title">HOW TO CREATE YOUR<br>OWN SIDE HUSTLE</h3>
  <div class="card-rule" style="top:208px"></div>
  <p class="card-text" style="top:220px">So, you’re thinking of starting a sidehustle, but before you do you should think about things definition, side hustles</p>
  <div class="btn-outline">Read More!</div>
</article>

<section class="course-band"></section>
<div class="checklist"><div class="checklist-art" role="img" aria-label="Nest &amp; Nook money checklist infographic listing banking, taxes, applications, saving and moving-out topics with tick boxes"></div></div>
<h2 class="course-title">WHY TAKE A<br>PERSONAL FINANCE COURSE?</h2>
<p class="course-text">Dorm Treasury will teach you how to use your student loan to get a new car, how to fill out those first day of work tax forms without calling mom and dad, and how to build credit without getting into credit card debt.</p>
<p class="course-cta">Personal financial skills will keep yourwallet full and your options open.Take charge of your finances today!</p>

<h2 class="section-title" style="top:2254px;font-size:26px">DON’T TAKE OUR WORD FOR IT…</h2>

<div class="quote-card" style="left:113px">
  <div class="quote-badge"><svg width="24" height="18" viewBox="0 0 24 18" fill="#fff"><path d="M0 18 V10 Q0 2 8 0 L9 3 Q4 5 4 9 H9 V18 Z M14 18 V10 Q14 2 22 0 L23 3 Q18 5 18 9 H23 V18 Z"/></svg></div>
  <div class="quote-body">
    <p class="quote-text">Believe it or not, I was fifty before I unders tood the difference between gross &amp; net was Dorm Treasury when I needed it</p>
    <p class="quote-author"><b>Daniel Hartley</b>, Founder of Northwind Group</p>
  </div>
</div>
<div class="quote-card" style="left:444px">
  <div class="quote-badge"><svg width="24" height="18" viewBox="0 0 24 18" fill="#fff"><path d="M0 18 V10 Q0 2 8 0 L9 3 Q4 5 4 9 H9 V18 Z M14 18 V10 Q14 2 22 0 L23 3 Q18 5 18 9 H23 V18 Z"/></svg></div>
  <div class="quote-body">
    <p class="quote-text">In today’s extra competitive job market, colle ge students need a leg up. Financial liter ac y skills, like those taught at Dorm Treasury, are the answer. Financial literacy provides</p>
    <p class="quote-author"><b>Lena Moravec</b>. Personal Finance Expert</p>
  </div>
</div>
<div class="quote-card" style="left:777px">
  <div class="quote-badge"><svg width="24" height="18" viewBox="0 0 24 18" fill="#fff"><path d="M0 18 V10 Q0 2 8 0 L9 3 Q4 5 4 9 H9 V18 Z M14 18 V10 Q14 2 22 0 L23 3 Q18 5 18 9 H23 V18 Z"/></svg></div>
  <div class="quote-body">
    <p class="quote-text">Having personally practiced in the area of personal financial planning for over thirty years, I am thrilled that there is finally a tool that my kids can use to learn</p>
    <p class="quote-author"><b>Paul Ostrander</b>, Parent</p>
  </div>
</div>

<section class="blog-section"></section>
<h2 class="section-title" style="top:2693px;font-size:30px">LATEST BLOG</h2>
<div class="title-rule"></div>

<article class="post-feature">
  <div class="thumb" role="img" aria-label="Photo of graduates throwing caps into a blue sky"></div>
  <div style="position:absolute;left:22px;right:22px;top:318px">
    <h3 class="post-title">How To Create Your Own Side Hustle</h3>
    <p class="post-meta" style="margin-top:20px">by DormTreasury | May 28, 2019 | How To</p>
    <p class="post-excerpt" style="margin-top:18px">So, you’re thinking of starting a side hustle, but before you do you should think about a few things. By definition, side hustles are any type of employment undertaken in addition to one’s full-time job…</p>
  </div>
</article>

<article class="post-small" style="top:2795px">
  <div class="thumb" role="img" aria-label="Photo of a student counting coins beside a piggy bank" style="background:linear-gradient(135deg,#6b5a4a,#b9a27f 60%,#8f9e9a)"></div>
  <div class="body">
    <h3 class="post-title">Money Saving Hacks For Millennials</h3>
    <p class="post-meta" style="margin-top:12px">by DormTreasury | May 28, 2019 | Hacks</p>
    <p class="post-excerpt" style="margin-top:10px">The other generations love to pick on us, but the unemployment rate is the lowest it’s been…</p>
  </div>
</article>
<article class="post-small" style="top:2962px">
  <div class="thumb" role="img" aria-label="Photo of a traveller with balloons on a car by the sea" style="background:linear-gradient(160deg,#3f86c0,#8cc0de 55%,#3e5566)"></div>
  <div class="body">
    <h3 class="post-title">How You Can Afford To Travel</h3>
    <p class="post-meta" style="margin-top:12px">by DormTreasury | May 28, 2019 | Hacks</p>
    <p class="post-excerpt" style="margin-top:10px">The other generations love to pick on us, but the unemployment rate is the lowest it’s been…</p>
  </div>
</article>
<article class="post-small" style="top:3132px">
  <div class="thumb" role="img" aria-label="Photo of a hand passing a payment card" style="background:linear-gradient(135deg,#e9e4de,#c9b8a6 50%,#3f6fb0)"></div>
  <div class="body">
    <h3 class="post-title">How To Budget</h3>
    <p class="post-meta" style="margin-top:12px">by DormTreasury | May 28, 2019 | Hacks</p>
    <p class="post-excerpt" style="margin-top:10px">The other generations love to pick on us, but the unemployment rate is the lowest it’s been…</p>
  </div>
</article>

<footer class="site-footer">
  <div class="footer-brand"><span class="brand-name">Dorm Treasury</span><span class="brand-dot"></span></div>
  <nav class="footer-nav"><span>Home</span>|<span>Take the Pledge</span>|<span>Blog</span>|<span>About Us</span>|<span>Tips &amp; Tricks</span>|<span>About Tallyvane</span></nav>
  <p class="copyright">© Copyright-2019 Dorm Treasury. All rights reserved.</p>
</footer>

</body>
</html>
```